Outdoor sign for Brindle Auto Restoration

I need a horizontal 4'x 8' outdoor roadside sign for my classic auto restoration business. I have uploaded colors and our logo. Needs the Brindle name, a prominent Classic AUTO RESTORATION, phone number and website. We rebuild and restore vintage cars, trucks and 4x4s. I'd like something clean but possibly retro. Classic Auto Restoration is more important than the Brindle name. It needs to be visible and readable from the street. NO CLIP ART

Target Market(s)

Customers who need their vintage care restored or upgraded. Men and women ages 25-75

Industry/Entity Type

Automotive

Colors
FFC000
F8CF3A
FAE287
FDF2CF
FEFAEE

Requirements
Must have
• Legible. Bright. Readable as a backlit 4' x 8' large horizontal sign (roughly 120cm X 240cm)
Nice to have
• Use of the Brindle logo/type, Complete or Classic before prominent AUTO RESTORATION
Should not have
• Clip art of old cars or icons. And we don't want the Brindle Logo from the website because it wont be legible from the road. I have included the Illustrator file for Brindle text in the uploads

```html
<!DOCTYPE html>
<html lang="en">
<head>
<meta charset="utf-8">
<title>Brindle Auto Restoration – Roadside Sign</title>
<link rel="stylesheet" href="https://fonts.googleapis.com/css2?family=Anton&family=Oswald:wght@700&display=swap">
<style>
  :root {
    --sign-yellow: #FFC000;
    --sign-blue: #04567C;
  }
  html, body {
    margin: 0;
    padding: 0;
    width: 1200px;
    height: 600px;
    overflow: hidden;
    background: var(--sign-yellow);
  }
  .sign {
    display: block;
    width: 1200px;
    height: 600px;
  }
  .sign__top-band { fill: var(--sign-yellow); }
  .sign__lower-panel { fill: var(--sign-blue); }
  .brand-name {
    font-family: 'Anton', Impact, sans-serif;
    fill: var(--sign-blue);
  }
  .headline {
    font-family: 'Anton', Impact, sans-serif;
    fill: var(--sign-yellow);
  }
  .kicker,
  .contact {
    font-family: 'Oswald', 'Arial Narrow', sans-serif;
    font-weight: 700;
    fill: var(--sign-yellow);
  }
  .icon-fill { fill: var(--sign-yellow); }
  .icon-line {
    fill: none;
    stroke: var(--sign-yellow);
    stroke-width: 4.5;
  }
</style>
</head>
<body>
<svg class="sign" viewBox="0 0 1200 600" xmlns="http://www.w3.org/2000/svg" aria-label="Brindle Complete Auto Restoration sign">
  <rect class="sign__top-band" x="0" y="0" width="1200" height="600"/>
  <path class="sign__lower-panel"
        d="M0 185 L426 200 L426 158 Q426 134 450 134 L753 134 Q777 134 777 158 L777 200 L1200 185 L1200 600 L0 600 Z"/>

  <text class="brand-name" x="330" y="116" font-size="104" textLength="532" lengthAdjust="spacingAndGlyphs">BRINDLE</text>

  <text class="kicker" x="450" y="212" font-size="66" textLength="300" lengthAdjust="spacingAndGlyphs">COMPLETE</text>

  <text class="headline" x="40" y="408" font-size="224" textLength="1114" lengthAdjust="spacingAndGlyphs">AUTO RESTORATION</text>

  <g class="contact-phone">
    <path class="icon-fill"
          d="M381 422 C372 424 364 430 360 442 C355 457 356 472 361 479 C366 486 376 488 383 486 C388 484 390 478 386 473 L380 465 C378 463 374 464 371 465 C368 462 368 448 371 445 C374 446 378 446 380 444 L386 435 C389 429 387 422 381 422 Z"/>
    <text class="contact" x="408" y="482" font-size="76" textLength="435" lengthAdjust="spacingAndGlyphs">501-555-0142</text>
  </g>

  <g class="contact-web">
    <circle class="icon-line" cx="109" cy="535" r="32"/>
    <ellipse class="icon-line" cx="109" cy="535" rx="14" ry="32"/>
    <line class="icon-line" x1="109" y1="503" x2="109" y2="567"/>
    <line class="icon-line" x1="77" y1="535" x2="141" y2="535"/>
    <line class="icon-line" x1="82" y1="520" x2="136" y2="520"/>
    <line class="icon-line" x1="82" y1="550" x2="136" y2="550"/>
    <text class="contact" x="164" y="565" font-size="78" textLength="954" lengthAdjust="spacingAndGlyphs">BRINDLEAUTOWORKS.COM</text>
  </g>
</svg>
</body>
</html>
```